Husband and i just started a new Hotshot trucking company, Its a pick up and delivery service. We own our own 40 foot gooseneck trailer... Called Roadbird Hauling LLC. We are needing some business cards made to help advertise our new company. We are based out of Ft Worth Tx. We are the ones who transports what ever loads to where ever they need to go, at any time. We stride for success. And we wont take no for an answer.
What we need on there is the following: need it to be all caps please.

DOUGLAS PRATHER "BO"
555-318-4426
ROADBIRDHAULINGLLC@MAILNEST.EXAMPLE

SHELBY CORWIN
555-604-7153

We have a couple logos already made. however we are always game to see new ideas. Thank you for your time.

Target Market(s)

Youth, middle aged. Home buyers

Industry/Entity Type

Hotshot Trucking Pick up and Delivery Service

Contact Information for Business Card

DOUGLAS PRATHER "BO" 555-318-4426 ROADBIRDHAULINGLLC@MAILNEST.EXAMPLE SHELBY CORWIN 555-604-7153 ROADBIRDHAULINGLLC@MAILNEST.EXAMPLE

Font styles to use
Serif
Script

Colors
0054AA
0677BA
7BADD7
CADEEF
E8F1F8
0094D4
00A9DD
6FCCEA
C7EBF8
E9F6FB

Requirements
Must have
• Our company logo. and look one of a kind. also has to be able to catch some ones eye and stand out
Nice to have
• open for ideas..

```html
<!DOCTYPE html>
<html lang="en">
<head>
<meta charset="utf-8">
<title>Roadbird Hauling LLC — Business Card</title>
<link rel="stylesheet" href="https://fonts.googleapis.com/css2?family=Lato:wght@400;700;900&display=swap">
<style>
  :root {
    --stage: #2f2f31;
    --card-front: #d4d5d8;
    --card-front-edge: #bfc0c4;
    --brand-blue: #0a6fd8;
    --blue-bright: #1487f0;
    --blue-deep: #001a66;
    --blue-night: #000d3d;
    --ink-light: #ffffff;
    --road-silver: #c9cbcf;
    --road-dark: #6b6d72;
    --truck-maroon: #7a1428;
  }
  * { box-sizing: border-box; margin: 0; padding: 0; }
  html, body {
    width: 1200px; height: 689px; overflow: hidden;
    background: var(--stage);
    font-family: "Lato", sans-serif;
  }
  .stage {
    position: relative; width: 1200px; height: 689px;
    display: flex; align-items: center; justify-content: center; gap: 50px;
  }
  .card {
    position: relative; width: 540px; height: 309px;
    border-radius: 22px; overflow: hidden;
    box-shadow: 0 18px 40px rgba(0,0,0,.55);
  }
  /* Front */
  .card-front {
    background: radial-gradient(circle at 40% 40%, var(--card-front) 0%, var(--card-front-edge) 100%);
    display: flex; align-items: center; justify-content: center;
  }
  .brand {
    display: flex; align-items: center; gap: 14px;
  }
  .brand-dot {
    width: 34px; height: 34px; border-radius: 50%;
    background: var(--brand-blue);
  }
  .brand-name {
    font-weight: 900; font-size: 30px; letter-spacing: .5px;
    color: var(--brand-blue); text-transform: uppercase;
  }
  /* Back */
  .card-back {
    background: linear-gradient(160deg, var(--blue-bright) 0%, var(--brand-blue) 25%, var(--blue-deep) 60%, var(--blue-night) 100%);
  }
  .scene-art {
    position: absolute; right: 0; bottom: 0; width: 540px; height: 309px;
  }
  .contacts {
    position: absolute; top: 34px; left: 30px; right: 26px;
    display: flex; justify-content: space-between;
    color: var(--ink-light);
  }
  .contact-name {
    font-weight: 700; font-size: 19px; letter-spacing: .3px;
    text-transform: uppercase; margin-bottom: 5px;
  }
  .contact-line {
    display: flex; align-items: center; gap: 8px;
    font-size: 15px; line-height: 1.45;
  }
  .contact-line.email { font-size: 12px; }
  .contact-line svg { width: 12px; height: 12px; flex: none; }
  .contact-secondary { margin-top: 0; }
</style>
</head>
<body>
<main class="stage">
  <section class="card card-front" aria-label="Card front">
    <div class="brand">
      <span class="brand-dot" aria-hidden="true"></span>
      <span class="brand-name">Roadbird Hauling LLC</span>
    </div>
  </section>

  <section class="card card-back" aria-label="Card back">
    <svg class="scene-art" viewBox="0 0 540 309" role="img" aria-label="Illustration of a maroon pickup truck towing a long gooseneck flatbed trailer on a silver road">
      <defs>
        <linearGradient id="road" x1="0" y1="0" x2="1" y2="1">
          <stop offset="0" stop-color="var(--road-dark)"/>
          <stop offset=".6" stop-color="var(--road-silver)"/>
          <stop offset="1" stop-color="#e6e7ea"/>
        </linearGradient>
        <linearGradient id="truck" x1="0" y1="0" x2="1" y2="0">
          <stop offset="0" stop-color="var(--truck-maroon)"/>
          <stop offset="1" stop-color="#5a5c62"/>
        </linearGradient>
      </defs>
      <polygon points="540,140 540,309 250,309" fill="url(#road)"/>
      <polygon points="150,309 150,215 250,150 540,150 540,200 330,309" fill="url(#truck)" opacity=".85"/>
    </svg>

    <div class="contacts">
      <div class="contact">
        <p class="contact-name">Douglas Prather "BO"</p>
        <p class="contact-line">
          <svg viewBox="0 0 12 12" aria-hidden="true"><rect x="3" y="1" width="6" height="10" rx="1" fill="none" stroke="#fff" stroke-width="1.2"/></svg>
          555-318-4426
        </p>
        <p class="contact-line email">
          <svg viewBox="0 0 12 12" aria-hidden="true"><rect x="1" y="2.5" width="10" height="7" fill="#fff"/><path d="M1 2.5 6 6.5 11 2.5" fill="none" stroke="#0a2a7a" stroke-width="1"/></svg>
          roadbirdhauling@mailnest.example
        </p>
      </div>
      <div class="contact contact-secondary">
        <p class="contact-name">Shelby Corwin</p>
        <p class="contact-line">
          <svg viewBox="0 0 12 12" aria-hidden="true"><rect x="3" y="1" width="6" height="10" rx="1" fill="none" stroke="#fff" stroke-width="1.2"/></svg>
          555-604-7153
        </p>
        <p class="contact-line email">
          <svg viewBox="0 0 12 12" aria-hidden="true"><rect x="1" y="2.5" width="10" height="7" fill="#fff"/><path d="M1 2.5 6 6.5 11 2.5" fill="none" stroke="#0a2a7a" stroke-width="1"/></svg>
          roadbirdhauling@mailnest.example
        </p>
      </div>
    </div>
  </section>
</main>
</body>
</html>
```